White Cane Law Awareness Poster

Bright Harbor is a disability advocacy organization in Indiana. We are working on a project with the Cedarbrook Society of Staff for Low Sight. Our organizations need a design for a poster to promote awareness of Indiana's White Cane law. This poster will be displayed in local libraries, businesses, and other public places.

The poster should catch people's attention, and briefly explain that drivers have to yield for pedestrians who are blind who have white canes or seeing eye dogs.

The poster should be designed with people with low vision in mind. This means large text in a clear font, with good contrast between the text and the background. The text should be in a sans serif font that is clear and easy to read, with no italics or script fonts. There should not be a "busy" picture or pattern behind the text.

The poster should also include a reference to the relevant laws. We have attached a document with those references.

Finally, the poster should include the logos of Bright Harbor and the Cedarbrook Society of Staff for Low Sight, which we have included as attachments.

We have also included an attachment with a photo of the old White Cane Law poster, just to show an example of what we DO NOT want.

Industry/Entity Type

Non-Profit

Font styles to use
Sans Serif

Requirements
Must have
• The poster should also include a reference to the relevant laws. We have attached a document with those references.
• Finally, the poster should include the logos of Bright Harbor and the Cedarbrook Society of Staff for Low Sight, which we have included as attachments.

```html
<!DOCTYPE html>
<html lang="en">
<head>
<meta charset="utf-8">
<title>White Cane Law Awareness Poster</title>
<link rel="stylesheet" href="https://fonts.googleapis.com/css2?family=Arimo:wght@400;700&display=swap">
<style>
  :root {
    --ink: #111111;
    --alert-red: #e8202a;
    --harbor-blue: #2b3fd6;
    --bg-light: #f4f4f4;
    --bg-mid: #d9d9d9;
    --paper: #ffffff;
  }
  * { margin: 0; padding: 0; box-sizing: border-box; }
  html, body { width: 800px; height: 1200px; overflow: hidden; }
  body { font-family: "Arimo", Arial, sans-serif; color: var(--ink); background: var(--paper); }

  .poster { position: relative; width: 800px; height: 1200px; overflow: hidden; }

  .backdrop {
    position: absolute; inset: 0;
    background:
      radial-gradient(ellipse 70% 40% at 20% 10%, var(--paper) 0%, transparent 70%),
      radial-gradient(ellipse 60% 35% at 85% 80%, var(--paper) 0%, transparent 70%),
      linear-gradient(160deg, var(--bg-mid) 0%, var(--bg-light) 35%, var(--bg-mid) 60%, var(--bg-light) 100%);
  }

  .partner-mark {
    position: absolute; left: 18px; top: 30px; width: 250px;
    display: flex; align-items: center; gap: 10px;
  }
  .partner-mark .dot { width: 34px; height: 34px; border-radius: 50%; background: var(--ink); flex: none; }
  .partner-mark .name { font-size: 17px; font-weight: 700; line-height: 1.25; color: var(--ink); }

  .host-mark {
    position: absolute; right: 14px; top: 60px;
    display: flex; align-items: center; gap: 12px;
  }
  .host-mark .dot { width: 40px; height: 40px; border-radius: 50%; background: var(--harbor-blue); flex: none; }
  .host-mark .name { font-size: 38px; font-weight: 700; color: var(--harbor-blue); }

  .alert-ring { position: absolute; left: 0; top: 0; width: 800px; height: 800px; }

  .alert-message {
    position: absolute; left: 80px; top: 298px; width: 624px;
    text-align: center; font-size: 35px; font-weight: 700; line-height: 44.4px;
  }

  .law-reference { position: absolute; left: 16px; top: 794px; width: 780px; }
  .law-reference h2 { font-size: 30px; font-weight: 700; line-height: 40px; }
  .law-reference p { font-size: 24.5px; line-height: 32.8px; }
  .law-reference .penalty { margin-top: 10px; }
</style>
</head>
<body>
<main class="poster">
  <div class="backdrop" role="img" aria-label="Soft grey and white flowing background"></div>

  <div class="partner-mark">
    <span class="dot"></span>
    <span class="name">Cedarbrook Society of Staff for Low Sight<br>Lakeside Chapter</span>
  </div>

  <div class="host-mark">
    <span class="dot"></span>
    <span class="name">Bright Harbor</span>
  </div>

  <svg class="alert-ring" viewBox="0 0 800 800" aria-hidden="true">
    <circle cx="390" cy="465" r="300" fill="var(--paper)" stroke="var(--alert-red)" stroke-width="38"/>
    <path d="M400 183 L456 280 L344 280 Z" fill="none" stroke="var(--ink)" stroke-width="9" stroke-linejoin="round"/>
    <rect x="395.5" y="212" width="9" height="38" rx="4.5" fill="var(--ink)"/>
    <circle cx="400" cy="262" r="6" fill="var(--ink)"/>
  </svg>

  <h1 class="alert-message">
    Indiana Law<br>requires<br>drivers to come to a<br>complete stop<br>when encountering a<br>pedestrian crossing a street<br>and guided by a<br>dog or carrying a<br>white cane
  </h1>

  <section class="law-reference">
    <h2>Indiana White Cane Law</h2>
    <p>Ind. Code § 9-21-17-21 : Indiana Code - Section 9-21-17-21:<br>Blind pedestrians; yield of right-of-way<br>A person who drives a vehicle shall yield the right-of-way to a<br>blind pedestrian carrying a clearly visible white cane or<br>accompanied by a guide dog.</p>
    <h2 class="penalty">Penalty</h2>
    <p>Ind. Code § 9-21-17-24 : Indiana Code - Section 9-21-17-24:<br>Violations; Class C infraction<br>A person who violates this chapter commits a Class C infraction.<br>(Misdemeanor)</p>
  </section>
</main>
</body>
</html>
```